依頼概要
■依頼目的 / 概要
電子書籍Lumora本を出版いたしますので、
表紙デザイン作成をお願いいたします。

■納品物
下記での納品をお願い致します。

JPEG形式 及び PSD形式
横1600ピクセル x 縦2560ピクセル

■本の内容

<本のタイトル>
ソラノワ-SKY RING-
老職人に学んだ
はじめての家庭づくりのガイドブック

<著者名>
浅井徹郎

■デザイン要望
・本のタイトル / 著者名の反映をお願いします

デザインイメージ

・基本的に青系の色合い

・シンプルな背景にタイトル等のコピーを記載

・ターゲットは子どもを持つご両親。

・お子様の子育てに関する細かいノウハウというよりも、
最も要となる考え方をお伝えしています。

・信頼感のあるデザインを希望します。

<表現したいイメージなど>
・信頼感

<表現したくないイメージ>
・安っぽい
・嘘くさい
・大衆的

<利用画像について>
画像素材を使用される場合には、
商用利用可の素材をお願いします。

■その他
デザインを考えるのに必要な情報が他にございましたら、
お答えしますので、遠慮なくご連絡ください。

*添付ファイルは、過去電子書籍の表紙デザインです。
*ジャンルが異なりますので、デザインテイストは今回とは、異なります。
*あくまでも、表紙に出てくる要素(タイトルや著者名など)の参考としてご利用ください。

意図をしっかりとご理解いただき、
目につく素晴らしいデザインに仕上げていただきました。
ありがとうございます。

この度は応募いただきありがとうございました。
近いうちにまた同じく、表紙のデザインをお願いする予定です。
またご参加くださいませ。

```html
<!DOCTYPE html>
<html lang="ja">
<head>
<meta charset="utf-8">
<title>ソラノワ-SKY RING- 表紙</title>
<link rel="stylesheet" href="https://fonts.googleapis.com/css2?family=Anton&family=Noto+Sans+JP:wght@500;700;900&display=swap">
<style>
  :root {
    --deep-blue: #17389a;
    --mid-blue: #2456c4;
    --sky-light: #cfe4f7;
    --sky-mid: #6fa2dc;
    --cyan: #4fd2f2;
    --ink: #111111;
    --paper: #ffffff;
  }
  * { margin: 0; padding: 0; box-sizing: border-box; }
  html, body { width: 750px; height: 1200px; overflow: hidden; background: var(--paper); }
  .cover {
    position: relative;
    width: 750px;
    height: 1200px;
    overflow: hidden;
    background: var(--paper);
    font-family: "Noto Sans JP", sans-serif;
  }
  .top-band {
    position: absolute;
    left: 0; top: 0;
    width: 750px; height: 475px;
    background: linear-gradient(160deg, var(--mid-blue) 0%, var(--deep-blue) 70%);
  }
  .photo-area {
    position: absolute;
    left: 0; top: 0;
    width: 750px; height: 1200px;
  }
  .series-title {
    position: absolute;
    left: 38px;
    top: 10px;
    font-family: "Anton", sans-serif;
    font-weight: 400;
    color: var(--paper);
    font-size: 200px;
    line-height: 1.1;
    letter-spacing: 6px;
    white-space: nowrap;
  }
  .series-title span { display: block; }
  .series-kana {
    position: absolute;
    left: 330px;
    top: 200px;
    color: var(--cyan);
    font-weight: 900;
    font-size: 48px;
    line-height: 1.2;
    letter-spacing: 2px;
    white-space: nowrap;
  }
  .author {
    position: absolute;
    left: 500px;
    top: 420px;
    color: var(--paper);
    font-weight: 700;
    font-size: 28px;
    line-height: 1.3;
    letter-spacing: 4px;
    white-space: nowrap;
  }
  .title-lead {
    position: absolute;
    left: 0; width: 750px;
    top: 482px;
    text-align: center;
    color: var(--ink);
    font-weight: 900;
    font-size: 76px;
    line-height: 1.2;
    letter-spacing: 2px;
    white-space: nowrap;
  }
  .title-main {
    position: absolute;
    left: 40px;
    top: 580px;
    display: flex;
    align-items: flex-end;
    gap: 12px;
    white-space: nowrap;
  }
  .title-tag {
    background: var(--deep-blue);
    color: var(--paper);
    font-weight: 700;
    font-size: 22px;
    line-height: 1.3;
    padding: 3px 8px;
    margin-bottom: 22px;
  }
  .title-word {
    color: var(--ink);
    font-weight: 900;
    font-size: 104px;
    line-height: 1.15;
  }
  .title-tail {
    position: absolute;
    left: 200px;
    top: 712px;
    color: var(--ink);
    font-weight: 900;
    font-size: 52px;
    line-height: 1.2;
    letter-spacing: 2px;
    white-space: nowrap;
  }
</style>
</head>
<body>
  <main class="cover">
    <div class="top-band"></div>

    <svg class="photo-area" width="750" height="1200" viewBox="0 0 750 1200" role="img" aria-label="青空を背景に親と子が手をつなぐ写真">
      <defs>
        <linearGradient id="sky" x1="0" y1="1" x2="1" y2="0">
          <stop offset="0" stop-color="#1d4fb6"/>
          <stop offset="0.55" stop-color="#6fa2dc"/>
          <stop offset="1" stop-color="#cfe4f7"/>
        </linearGradient>
      </defs>
      <path d="M0 760 C150 770 260 800 360 850 C470 900 560 820 640 720 C690 640 720 560 750 520 L750 470 C700 500 640 560 600 640 C560 720 500 780 420 790 C300 800 150 750 0 730 Z" fill="url(#sky)" opacity="0.55"/>
      <path d="M0 800 C160 810 280 860 380 920 C470 970 530 1000 560 1060 L580 1200 L0 1200 Z" fill="url(#sky)"/>
    </svg>

    <h1 class="series-title" aria-label="SKY RING"><span>SKY</span><span>RING</span></h1>
    <p class="series-kana">ソラノワ</p>
    <p class="author">浅井 徹郎</p>

    <p class="title-lead">老職人に学んだ</p>
    <div class="title-main">
      <span class="title-tag">はじめての</span>
      <span class="title-word">家庭づくり</span>
    </div>
    <p class="title-tail">のガイドブック</p>
  </main>
</body>
</html>
```